LRV Fitness Supplements Container Label

We are a veteran owned fitness supplement company, we would like to create a universal label for our product line where we can just chasnge out the product name and flavor and a block for ingredients label. We would like it to be almost all black and white/grey. The ends of the labels we would like to be wrapped in a black multicam background. We would like our company logo on it, and our product name is "IRON DAWN". Bottom right corner say
Distributed by:
Bramwell Vitality Supplements
4172 Orchard Bend
Ashgrove, Pa 16099
www.bramwellvitalitysupplements.example
Then our logo again. Below that, "Proudly made in the USA" with a small american flag.

```html
<!DOCTYPE html>
<html lang="en">
<head>
<meta charset="utf-8">
<title>LRV Fitness Supplements – Iron Dawn Label</title>
<link href="https://fonts.googleapis.com/css2?family=Arimo:wght@400;700&family=Russo+One&display=swap" rel="stylesheet">
<style>
  :root{
    --page:#ffffff;
    --ink:#111111;
    --black:#0d0d0d;
    --white:#ffffff;
    --camo-dark:#1c201b;
    --camo-mid:#3a4236;
    --grey-text:#6a6a6a;
    --glue:#e6e6e6;
    --mark:#9a9a9a;
  }
  *{box-sizing:border-box;margin:0;padding:0}
  html,body{width:1200px;height:1200px;overflow:hidden;background:var(--page)}
  body{position:relative;font-family:"Arimo",Arial,sans-serif;color:var(--ink)}
  .abs{position:absolute}

  .crop{position:absolute;background:var(--mark)}
  .crop.h{height:1px;width:14px}
  .crop.v{width:1px;height:12px}

  .glue-area{left:108px;top:398px;width:22px;height:382px;background:var(--glue)}
  .glue-area span{position:absolute;left:4px;bottom:14px;writing-mode:vertical-rl;transform:rotate(180deg);font-size:9px;color:#999}

  .camo{left:130px;top:398px;width:963px;height:382px;
    background:
      radial-gradient(ellipse 60px 30px at 20% 30%,var(--camo-mid),transparent 70%),
      radial-gradient(ellipse 70px 35px at 75% 70%,var(--camo-mid),transparent 70%),
      radial-gradient(ellipse 50px 28px at 90% 20%,var(--camo-mid),transparent 70%),
      linear-gradient(135deg,#232821,var(--camo-dark) 50%,#262b24);}

  .tag{background:var(--white)}
  .tag::before,.tag::after{content:"";position:absolute;left:0;right:0;height:7px;
    background:repeating-linear-gradient(90deg,var(--camo-dark) 0 5px,transparent 5px 11px)}
  .tag::before{top:0}
  .tag::after{bottom:0}
  .tag-benefits{left:215px;top:436px;width:220px;height:299px;background:linear-gradient(90deg,#fff,#f2f2f2 70%,#dedede)}
  .tag-facts{left:820px;top:436px;width:192px;height:297px}

  .benefits{left:232px;top:488px;transform:rotate(-8deg);transform-origin:left top;font-size:19px;line-height:28px;list-style:none}
  .benefits li{display:flex;align-items:center;gap:5px;white-space:nowrap}
  .benefits li:nth-child(2){padding-left:48px}
  .benefits li:nth-child(3){padding-left:56px}
  .benefits li:nth-child(4){padding-left:4px}
  .tick{width:13px;height:13px;border:1.5px solid var(--ink);position:relative;flex:none}
  .tick::after{content:"";position:absolute;left:2px;top:-4px;width:5px;height:10px;border:solid var(--ink);border-width:0 2px 2px 0;transform:rotate(40deg)}

  .front{left:435px;top:398px;width:330px;height:382px;background:linear-gradient(180deg,#fff,#f4f4f4)}
  .brand{left:435px;top:418px;width:330px;text-align:center}
  .brand .name{font-weight:700;font-size:28px;letter-spacing:2px;color:var(--ink);line-height:28px}
  .brand .sub{font-size:4.5px;letter-spacing:.5px;margin-top:2px}
  .origin{left:435px;top:458px;width:330px;text-align:center;font-size:7px;line-height:8px}
  .flag{display:block;margin:2px auto 0;width:16px;height:9px;background:repeating-linear-gradient(180deg,#b22234 0 1.3px,#fff 1.3px 2.6px);position:relative}
  .flag::before{content:"";position:absolute;left:0;top:0;width:7px;height:5px;background:#3c3b6e}

  .title-bar{left:460px;width:276px;height:7px;
    background:linear-gradient(90deg,#fff 0,#e4e4e4 25%,#bdbdbd 50%,#7a7a7a 75%,#111 100%)}
  .title-bar.top{top:553px}
  .title-bar.bottom{top:614px}
  .title{left:460px;top:560px;width:276px;text-align:center;font-family:"Russo One",sans-serif;font-size:42px;line-height:52px;color:var(--ink);text-shadow:3px 3px 0 #9c9c9c;white-space:nowrap}
  .flavor{left:560px;top:631px;width:176px;text-align:right;font-size:21px;color:var(--grey-text)}
  .tagline{left:435px;top:663px;background:var(--black);color:var(--white);font-size:11px;padding:4px 10px 4px 12px;letter-spacing:.3px}

  .panel-black{left:435px;top:695px;width:330px;height:85px;background:var(--black)}
  .badge{left:452px;top:706px;width:63px;height:23px;background:#6b6b6b;color:var(--white);font-size:8.5px;line-height:9px;padding:3px 4px}
  .badge-dots{left:517px;top:704px;width:8px;height:8px;background:
    linear-gradient(#777,#777) 0 4px/4px 4px no-repeat,linear-gradient(#777,#777) 4px 0/4px 4px no-repeat}
  .netwt{left:452px;top:742px;font-size:10.5px;color:var(--white)}
  .dist{left:579px;top:702px;font-size:7.5px;line-height:9.5px;color:var(--white)}

  .facts{left:849px;top:450px;width:158px;font-size:8.5px}
  .facts h3{font-size:8.5px;font-weight:400;border-bottom:1px solid #888;padding-bottom:4px;margin-bottom:14px}
  .facts table{width:100%;border-collapse:collapse}
  .facts td{padding:1px 0;line-height:13px;white-space:nowrap}
  .facts td.qty{text-align:right}
  .facts section+section{margin-top:22px}
</style>
</head>
<body>
  <i class="crop h" style="left:95px;top:405px"></i>
  <i class="crop h" style="left:95px;top:773px"></i>
  <i class="crop v" style="left:115px;top:385px"></i>
  <i class="crop v" style="left:1093px;top:385px"></i>
  <i class="crop v" style="left:115px;top:782px"></i>
  <i class="crop v" style="left:1093px;top:782px"></i>

  <div class="abs glue-area"><span>Glue Area</span></div>
  <div class="abs camo" role="img" aria-label="Black multicam camouflage pattern wrapping the label ends"></div>

  <div class="abs tag tag-benefits"></div>
  <ul class="abs benefits">
    <li><i class="tick"></i>Increased Strength</li>
    <li><i class="tick"></i>Body Immune</li>
    <li><i class="tick"></i>Power Output</li>
    <li><i class="tick"></i>Great Performance</li>
  </ul>

  <div class="abs front"></div>
  <svg class="abs" style="left:435px;top:398px" width="330" height="180" viewBox="0 0 330 180">
    <polyline points="25,0 165,118 305,0" fill="none" stroke="#8a8a8a" stroke-width="9"/>
    <polyline points="45,0 165,100 285,0" fill="none" stroke="#d0d0d0" stroke-width="4"/>
    <polygon points="330,30 330,60 180,160 160,150" fill="#c8c8c8"/>
  </svg>
  <div class="abs brand"><div class="name">LRV</div><div class="sub">LRV FITNESS SUPPLEMENTS</div></div>
  <div class="abs origin">Proudly<br>Made in the USA<i class="flag" role="img" aria-label="Small American flag"></i></div>

  <div class="abs title-bar top"></div>
  <div class="abs title-bar bottom"></div>
  <div class="abs title">IRON DAWN</div>
  <div class="abs flavor">Cream Melon</div>
  <div class="abs tagline">NATURALY &amp; HEALTH</div>

  <div class="abs panel-black"></div>
  <div class="abs badge">BODY<br>SUPPLEMENT</div>
  <i class="abs badge-dots"></i>
  <div class="abs netwt">NET WT 10.6 OZ (300 g)</div>
  <div class="abs dist">Distributed by :<br>Bramwell Vitality Supplements<br>4172 Orchard Bend<br>Ashgrove, Pa 16099<br>www.bramwellvitalitysupplements.example</div>

  <div class="abs tag tag-facts"></div>
  <div class="abs facts">
    <section>
      <h3>Ingredients</h3>
      <table>
        <tr><td>Nam at sagittis elit</td><td class="qty">0.5 gr</td></tr>
        <tr><td>Neque porro quisquam</td><td class="qty">100 gr</td></tr>
        <tr><td>consectetur adipiscing elit</td><td class="qty">99 gr</td></tr>
        <tr><td>Curabitur vitae ultrices</td><td class="qty">32 gr</td></tr>
        <tr><td>Mauris a lorem ac nulla</td><td class="qty">0.9 gr</td></tr>
      </table>
    </section>
    <section>
      <h3>Nutrient Content</h3>
      <table>
        <tr><td>Nam at sagittis elit</td><td class="qty">0.5 gr</td></tr>
        <tr><td>Neque porro quisquam</td><td class="qty">100 gr</td></tr>
        <tr><td>consectetur adipiscing elit</td><td class="qty">99 gr</td></tr>
        <tr><td>Curabitur vitae ultrices</td><td class="qty">32 gr</td></tr>
        <tr><td>Mauris a lorem ac nulla</td><td class="qty">0.9 gr</td></tr>
      </table>
    </section>
  </div>
</body>
</html>
```